Business card and stationary for a garage
Motorwerkplaats Lindeveld
@ph - changes done .Please check and confirm.- Thanks
@quickdraft
Can you please make another version with #136 as the front and #135 as the back side.
Note 1: Please omit the word "Services" and make the logo a little bit bigger at the back side
Note 2: It's Merelhoflaan
Note 3: #135 the back side. The text "Motorwerkplaats Lindeveld" is too gray. Just use the original logo and colors.
#ALL
Please use "T" for phonenumber and "F" for fax. Do not use the English abbreviations. Or better use icons.
Nice designs, thank you.
We dont prefer a style like #124-#129 for the back of the card. Its to simple. The service listing can be more attractive like in #121 or #118 (horizontal).
#ALL please do not use english words in business card like "Our services". Use only "Services" as this is also a common word in Dutch.
"Voor alle merken" means "For all brands"

```html
<!DOCTYPE html>
<html lang="nl">
<head>
<meta charset="utf-8">
<title>Motorwerkplaats Lindeveld – visitekaartje</title>
<link rel="stylesheet" href="https://fonts.googleapis.com/css2?family=Arimo:wght@400;700&display=swap">
<style>
  :root {
    --stage: #3a3a3c;
    --red: #c8161d;
    --red-dark: #8e0d12;
    --red-light: #e0282e;
    --white: #ffffff;
    --paper: #f4f4f4;
    --ink: #2b2b2b;
    --grey: #8a8a8a;
    --swoosh: #d6d6d6;
  }
  * { box-sizing: border-box; margin: 0; padding: 0; }
  html, body { width: 1200px; height: 874px; overflow: hidden; }
  body {
    background: var(--stage);
    font-family: "Arimo", Arial, sans-serif;
    display: flex;
    align-items: center;
    justify-content: center;
    gap: 60px;
  }
  .card {
    position: relative;
    width: 520px;
    height: 310px;
    border-radius: 4px;
    overflow: hidden;
    box-shadow: 0 14px 30px rgba(0,0,0,.45);
  }

  /* Front */
  .card--front {
    background: radial-gradient(ellipse at 30% 30%, var(--red-light), var(--red) 55%, var(--red-dark));
    color: var(--white);
  }
  .card--front .brand {
    position: absolute;
    left: 48px; top: 70px;
    display: flex; align-items: center; gap: 14px;
  }
  .brand__square {
    width: 46px; height: 46px;
    background: var(--white);
  }
  .card--front .brand__name {
    font-weight: 700; font-size: 26px; letter-spacing: .5px;
    text-transform: uppercase; line-height: 1.05; width: 300px;
  }
  .services-title {
    position: absolute; left: 48px; top: 168px;
    font-size: 17px; font-weight: 400;
  }
  .services {
    position: absolute; left: 48px; top: 210px;
    display: flex; gap: 26px; list-style: none;
    font-size: 13px;
  }
  .services li::before { content: "• "; }
  .tagline {
    position: absolute; left: 48px; top: 244px;
    font-size: 13px;
  }

  /* Back */
  .card--back { background: var(--paper); color: var(--ink); }
  .card--back .decor { position: absolute; inset: 0; }
  .card--back .brand {
    position: absolute; left: 36px; top: 120px;
    display: flex; align-items: center; gap: 12px;
  }
  .card--back .brand__square { background: var(--red); width: 40px; height: 40px; }
  .card--back .brand__name {
    font-weight: 700; font-size: 19px; text-transform: uppercase;
    color: var(--ink); width: 200px; line-height: 1.1;
  }
  .contact {
    position: absolute; left: 320px; top: 72px;
    font-size: 11.5px; line-height: 1.6;
  }
  .contact__name {
    color: var(--red); font-weight: 700; font-size: 16px; margin-bottom: 10px;
  }
  .contact__gap { margin-top: 8px; }
  .website {
    position: absolute; left: 0; right: 0; bottom: 10px;
    text-align: center; color: var(--white);
    font-size: 12px; letter-spacing: 3px;
  }
</style>
</head>
<body>

  <section class="card card--front" aria-label="Voorkant">
    <div class="brand">
      <span class="brand__square"></span>
      <span class="brand__name">Motorwerkplaats Lindeveld</span>
    </div>
    <h2 class="services-title">Services</h2>
    <ul class="services">
      <li>Onderhoud</li>
      <li>APK</li>
      <li>Banden</li>
      <li>Airco</li>
    </ul>
    <p class="tagline">Voor alle merken</p>
  </section>

  <section class="card card--back" aria-label="Achterkant">
    <svg class="decor" width="520" height="310" viewBox="0 0 520 310" aria-hidden="true">
      <path d="M0 0 H520 V48 C400 40 330 60 250 86 C170 110 80 100 0 70 Z" fill="var(--red)"/>
      <path d="M0 78 C80 108 170 118 250 94 C330 70 410 50 520 56 V62 C410 58 330 80 250 104 C170 126 80 118 0 90 Z" fill="var(--swoosh)"/>
      <path d="M0 280 C150 266 360 266 520 276 V310 H0 Z" fill="var(--red)"/>
    </svg>
    <div class="brand">
      <span class="brand__square"></span>
      <span class="brand__name">Motorwerkplaats Lindeveld</span>
    </div>
    <address class="contact" style="font-style:normal">
      <p class="contact__name">Ruben Kessels</p>
      <p>Merelhoflaan 23</p>
      <p>3702 KL Lindeveld</p>
      <p class="contact__gap">T: 030-4418205</p>
      <p>F: 030-4418206</p>
      <p>E: info@bolwerkxq.nl</p>
    </address>
    <p class="website">www.bolwerkxq.nl</p>
  </section>

</body>
</html>
```